Home Design company focused on remodel and enhancement of kitchens and bathroorms

I already have a logo designed by ArtHarbor, I now need a design for my business cards.
The company is in the remodeling and enhancement industry for homes, focusing on kitchens and bathrooms, however, we can remodel or enhance every room in a home, an office space, etc.

The company's name is VELMOR HOME DESIGN, LLC

We'll focus on clients in the Rio Grande Valley, Texas. Primarily McAllen, Edinburg, Pharr, Mission, Brownsville and South Padre Island.

The design on the business card should transmit reliability, professionalism anda bit of upscale design.

The logo is in black and white, and would like to keep it that way.

The information that needs to be printed in the business cards is:
Company's name: Velmor Home Design
Company's Logo (attached)
My name: Noel Bramwit
Address, phone and email:
2715 N Parkline Road, Ste 348
Larkhaven, ST 10101
(555) 010 0187
nbramwit@velmordesign.example
Website: velmordesign.example

```html
<!DOCTYPE html>
<html lang="en">
<head>
<meta charset="utf-8">
<title>Velmor Home Design — Business Card</title>
<link rel="stylesheet" href="https://fonts.googleapis.com/css2?family=Montserrat:wght@400;500&family=Playfair+Display:wght@500&family=Arimo:wght@400&display=swap">
<style>
  :root {
    --page: #ffffff;
    --paper: #fbfbfb;
    --edge: #3a3a3a;
    --ink: #000000;
    --slate: #575757;
    --light: #ffffff;
    --text-dark: #1a1a1a;
  }
  * { margin: 0; padding: 0; box-sizing: border-box; }
  html, body {
    width: 1200px; height: 1200px; overflow: hidden;
    background: var(--page);
  }
  .sheet {
    position: relative; width: 1200px; height: 1200px;
    display: flex; flex-direction: column; align-items: center;
    justify-content: space-evenly;
  }
  .card {
    position: relative; width: 880px; height: 518px;
    background: var(--paper);
    border: 1px solid var(--edge);
    overflow: hidden;
  }
  .band { position: absolute; }
  .band--black { left: 0; top: 104px; width: 607px; height: 155px; background: var(--ink); }
  .band--slate { left: 289px; top: 259px; right: 0; height: 150px; background: var(--slate); }

  .brand-mark {
    position: absolute; left: 197px; top: 150px;
    font-family: "Montserrat", sans-serif; font-weight: 400;
    font-size: 50px; letter-spacing: 0.12em; color: var(--light);
    line-height: 1;
  }
  .company-name {
    position: absolute; left: 486px; top: 276px;
    font-family: "Montserrat", sans-serif; font-weight: 400;
    font-size: 33px; line-height: 40px; letter-spacing: 0.2em;
    color: var(--light); text-transform: uppercase;
  }
  .website {
    position: absolute; left: 299px; top: 444px;
    font-family: "Montserrat", sans-serif; font-weight: 500;
    font-size: 16px; letter-spacing: 0.2em; color: var(--text-dark);
  }

  .person-name {
    position: absolute; left: 55px; top: 151px;
    font-family: "Playfair Display", serif; font-weight: 500;
    font-size: 40px; letter-spacing: 0.06em; line-height: 1;
    color: var(--light); text-transform: uppercase;
  }
  .person-title {
    position: absolute; left: 57px; top: 196px;
    font-family: "Montserrat", sans-serif; font-weight: 500;
    font-size: 17px; letter-spacing: 0.28em; color: var(--light);
  }
  .contact {
    position: absolute; right: 50px; top: 283px;
    text-align: right; list-style: none;
    font-family: "Arimo", sans-serif; font-size: 17px;
    line-height: 27.5px; letter-spacing: 0.14em; color: var(--light);
  }
</style>
</head>
<body>
<main class="sheet">
  <section class="card card--front" aria-label="Business card front">
    <div class="band band--black"></div>
    <div class="band band--slate"></div>
    <div class="brand-mark">VELMOR</div>
    <h1 class="company-name">Velmor<br>Home<br>Design</h1>
    <p class="website">www.velmordesign.example</p>
  </section>

  <section class="card card--back" aria-label="Business card back">
    <div class="band band--black"></div>
    <div class="band band--slate"></div>
    <h2 class="person-name">Noel Bramwit</h2>
    <p class="person-title">FOUNDER</p>
    <ul class="contact">
      <li>2715 N Parkline Road, Ste 348</li>
      <li>Larkhaven, ST 10101</li>
      <li>(555) 010 0187</li>
      <li>nbramwit@velmordesign.example</li>
    </ul>
  </section>
</main>
</body>
</html>
```